BRH 2014 Seasons Greetings

Christmas postcards.
Side A: Image with 3 logos "Varek Cove Lodge" "Mirufa Lodge Samoa" "Keli Vasa"(Logos on bottom of card" & "Seasons Greetings" (to fit)
Side B Left:
Text
"Management and staff at Corvina Lodges wish you and your family a very happy and safe festive season and all the best for the New Year.
Counting down your next arrival"
Side B Right: Address template with 4 lines & Area for stamp top right corner.
Side B Base: Logo & Website "Corvina Lodges" " www.corvinalodges.example"
Target Market(s)
High end travel
Industry/Entity Type
Management
Look and feel
Each slider illustrates characteristics of the customer's brand and the style your logo design should communicate.

```html
<!DOCTYPE html>
<html lang="en">
<head>
<meta charset="utf-8">
<title>Corvina Lodges – Season's Greetings Postcard</title>
<link href="https://fonts.googleapis.com/css2?family=Jost:wght@300;400;500&family=Hind:wght@300;400&display=swap" rel="stylesheet">
<style>
  :root {
    --bg-orange-light: #f9a21c;
    --bg-orange-dark: #ec7a12;
    --card-white: #ffffff;
    --ink-grey: #9b9b9b;
    --rule-grey: #8a8a8a;
    --ink-dark: #1d1d1d;
    --ink-white: #ffffff;
    --night: #0c130f;
    --dusk-top: #2a2f8c;
    --dusk-bottom: #5e6fb8;
    --sky-pale: #e4e7ee;
    --wave-blue: #3fa4c8;
    --sand: #d9d1c6;
  }
  * { box-sizing: border-box; margin: 0; padding: 0; }
  html, body { width: 800px; height: 1200px; overflow: hidden; }
  body {
    position: relative;
    background: radial-gradient(ellipse at 50% 35%, var(--bg-orange-light) 0%, var(--bg-orange-dark) 85%);
    font-family: "Hind", sans-serif;
  }

  .postcard {
    position: absolute;
    left: 52px;
    width: 712px;
    height: 553px;
    box-shadow: 2px 3px 6px rgba(0,0,0,0.35);
  }
  .postcard--front { top: 34px; background: var(--night); overflow: hidden; }
  .postcard--back { top: 613px; background: var(--card-white); }

  /* Front photo grid */
  .photo { position: absolute; }
  .photo--fireworks {
    left: 0; top: 0; width: 341px; height: 553px;
    background: radial-gradient(ellipse at 45% 45%, #3b2a12 0%, #14331d 35%, var(--night) 75%);
  }
  .photo--sunset {
    left: 341px; top: 0; width: 371px; height: 204px;
    background: linear-gradient(180deg, var(--dusk-top) 0%, var(--dusk-bottom) 55%, #3a3f7a 70%, #1f2350 100%);
  }
  .photo--toast {
    left: 341px; top: 204px; width: 180px; height: 124px;
    background: linear-gradient(135deg, var(--sky-pale) 0%, #e9c7b4 45%, #d8d6dc 100%);
  }
  .photo--wave {
    left: 521px; top: 204px; width: 191px; height: 124px;
    background: linear-gradient(180deg, #c9e6f0 0%, var(--wave-blue) 55%, #8fd0e0 100%);
  }
  .photo--sand {
    left: 341px; top: 328px; width: 371px; height: 225px;
    background: linear-gradient(160deg, #e2dbd1 0%, var(--sand) 60%, #cfc6ba 100%);
  }

  .front-title {
    position: absolute;
    left: 50px; top: 52px;
    font-family: "Jost", sans-serif;
    font-weight: 300;
    font-size: 37px;
    letter-spacing: 2px;
    color: var(--ink-white);
    white-space: nowrap;
  }

  .lodge-names {
    position: absolute;
    left: 62px; top: 444px;
    display: flex; flex-direction: column; gap: 3px;
    font-family: "Jost", sans-serif;
    font-weight: 400;
    font-size: 11px;
    line-height: 13px;
    color: var(--ink-white);
    letter-spacing: 0.4px;
  }
  .lodge-names__row { display: flex; align-items: center; gap: 6px; white-space: nowrap; }
  .lodge-names__dot { width: 8px; height: 8px; border: 1.5px solid var(--ink-white); border-radius: 50%; }
  .front-url {
    position: absolute;
    left: 55px; top: 498px;
    font-family: "Jost", sans-serif;
    font-size: 13px;
    color: var(--ink-white);
    white-space: nowrap;
  }

  .brand {
    position: absolute;
    display: flex; align-items: center; gap: 10px;
    font-family: "Jost", sans-serif;
    white-space: nowrap;
  }
  .brand__mark { width: 10px; height: 10px; }
  .brand__name { font-weight: 400; }
  .brand--front { left: 420px; top: 496px; font-size: 14px; letter-spacing: 2px; color: var(--ink-dark); }
  .brand--front .brand__mark { background: var(--ink-dark); }
  .brand--back { left: 88px; top: 68px; font-size: 11.5px; letter-spacing: 1.4px; color: var(--ink-grey); }
  .brand--back .brand__mark { background: var(--ink-grey); }

  /* Back */
  .divider {
    position: absolute;
    left: 344px; top: 38px;
    width: 1px; height: 473px;
    background: var(--rule-grey);
  }
  .greeting {
    position: absolute;
    left: 50px; top: 194px;
    width: 272px;
    font-weight: 300;
    font-size: 16px;
    line-height: 20px;
    color: var(--ink-grey);
    text-align: justify;
  }
  .greeting__signoff { margin-top: 20px; text-align: left; }
  .website {
    position: absolute;
    left: 50px; top: 420px;
    font-weight: 300;
    font-size: 21px;
    color: var(--ink-grey);
    letter-spacing: 0.2px;
    white-space: nowrap;
  }
  .address-line {
    position: absolute;
    left: 376px;
    width: 270px; height: 1px;
    background: var(--rule-grey);
  }
  .address-line--1 { top: 229px; }
  .address-line--2 { top: 291px; }
  .address-line--3 { top: 344px; }
  .address-line--4 { top: 400px; }
</style>
</head>
<body>

<section class="postcard postcard--front">
  <div class="photo photo--fireworks" role="img" aria-label="Fireworks bursting over palm trees on a beach at night"></div>
  <div class="photo photo--sunset" role="img" aria-label="Sunset over a calm bay with moored boats and a small island"></div>
  <div class="photo photo--toast" role="img" aria-label="Guest raising a can of beer toward the camera"></div>
  <div class="photo photo--wave" role="img" aria-label="View from inside a breaking turquoise wave toward an island"></div>
  <div class="photo photo--sand" role="img" aria-label="Lodge name spelled out with driftwood and shells on white sand"></div>

  <h1 class="front-title">SEASON’S GREETINGS!</h1>

  <div class="lodge-names">
    <div class="lodge-names__row"><span class="lodge-names__dot"></span><span>Varek Cove Lodge</span></div>
    <div class="lodge-names__row"><span class="lodge-names__dot"></span><span>Mirufa Lodge Samoa</span></div>
    <div class="lodge-names__row"><span class="lodge-names__dot"></span><span>Keli Vasa</span></div>
  </div>
  <div class="front-url">varekcovelodge.example</div>

  <div class="brand brand--front">
    <span class="brand__mark"></span>
    <span class="brand__name">CORVINA LODGES &amp; RESORTS</span>
  </div>
</section>

<section class="postcard postcard--back">
  <div class="brand brand--back">
    <span class="brand__mark"></span>
    <span class="brand__name">CORVINA LODGES &amp; RESORTS</span>
  </div>

  <div class="greeting">
    <p>Management and staff at Corvina Lodges wish you and your family a very happy and safe festive season and all the best for the New Year.</p>
    <p class="greeting__signoff">Counting down your next arrival</p>
  </div>

  <div class="website">www.corvinalodges.example</div>

  <div class="divider"></div>

  <div class="address-line address-line--1"></div>
  <div class="address-line address-line--2"></div>
  <div class="address-line address-line--3"></div>
  <div class="address-line address-line--4"></div>
</section>

</body>
</html>
```